Medical Transportation Company Brochure

I need a brochure for a medical transportation company called CareSwift Transit Health Services that provides ambulance and mobility assistance vehicle transportation services to and from healthcare facilities as well as event standby and healthcare training through our training center (cpr, professional continuing education courses). Id like something that incorporates our company logo's colors and looks eye catching yet sleek and professional

Target Market(s)

Patients, healthcare facilities

Industry/Entity Type

Medical

Font styles to use
Sans Serif

Requirements
Must have
• Flyer must have a description of our services as well as text that is easy to read, be visually captivating and stand out, include our contact information and process to book appointment for transport with us

```html
<!DOCTYPE html>
<html lang="en">
<head>
<meta charset="utf-8">
<title>CareSwift Transit Health Services – Flyer</title>
<link rel="stylesheet" href="https://fonts.googleapis.com/css2?family=Bebas+Neue&family=Open+Sans:wght@400;600&display=swap">
<style>
  :root {
    --red: #b31f2b;
    --red-dark: #951822;
    --navy: #1f2d5c;
    --gold: #f2a51a;
    --white: #ffffff;
    --photo-blue: #5f7fa6;
  }
  * { margin: 0; padding: 0; box-sizing: border-box; }
  html, body { width: 978px; height: 1200px; overflow: hidden; background: #ffffff; }
  .flyer {
    position: relative; width: 978px; height: 1200px; overflow: hidden;
    background: var(--red); font-family: "Open Sans", Arial, sans-serif; color: var(--white);
  }
  .hero-shapes { position: absolute; left: 0; top: 0; width: 978px; height: 600px; }
  .badge-24 { position: absolute; left: 790px; top: 28px; width: 150px; height: 110px; }
  .headline {
    position: absolute; right: 30px; top: 318px; text-align: right;
    font-family: "Bebas Neue", Impact, sans-serif; font-size: 54px; line-height: 72px; letter-spacing: 1px;
    text-shadow: 0 2px 4px rgba(0,0,0,.25);
  }
  .intro {
    position: absolute; right: 30px; top: 472px; width: 520px; text-align: right;
    font-size: 15.5px; line-height: 21px;
  }
  .services { position: absolute; left: 0; top: 600px; width: 978px; height: 190px; display: flex; padding: 0 20px; }
  .service {
    flex: 1; display: flex; flex-direction: column; align-items: center; padding-top: 22px;
    border-right: 2px dotted rgba(255,255,255,.35);
  }
  .service:last-child { border-right: none; }
  .service svg { width: 64px; height: 54px; }
  .service-label {
    margin-top: 32px; text-align: center;
    font-family: "Bebas Neue", Impact, sans-serif; font-size: 29px; line-height: 36px; letter-spacing: .5px;
  }
  .divider { position: absolute; left: 0; top: 803px; width: 978px; height: 3px; background: var(--white); }
  .gallery { position: absolute; left: 0; top: 806px; width: 978px; height: 242px; background: var(--navy); }
  .gallery-photo { position: absolute; top: 4px; height: 236px; width: 292px; }
  .photo-stretcher { left: 45px; background: linear-gradient(160deg, #c9ccd0, #8d9aa3 60%, #b3282f); }
  .photo-standby { left: 348px; background: linear-gradient(170deg, #6e7d88, #2a3240 55%, #5f8a45); }
  .photo-paramedic { left: 652px; background: linear-gradient(160deg, #d4c9b8, #c8c74a 55%, #394250); }
  .footer { position: absolute; left: 0; top: 1048px; width: 978px; height: 152px; background: var(--white); }
  .footer-shapes { position: absolute; left: 0; top: 0; width: 978px; height: 152px; }
  .brand {
    position: absolute; left: 40px; top: 30px; display: flex; align-items: center; gap: 14px;
    font-family: "Bebas Neue", Impact, sans-serif; color: var(--navy);
  }
  .brand-mark { width: 30px; height: 30px; border-radius: 50%; background: var(--navy); }
  .brand-name { font-size: 40px; line-height: 38px; letter-spacing: .5px; }
  .contact { position: absolute; left: 548px; top: 38px; }
  .phone-line { display: flex; align-items: center; gap: 18px; }
  .phone-icon { width: 28px; height: 44px; }
  .phone {
    font-family: "Bebas Neue", Impact, sans-serif; font-size: 58px; line-height: 58px; letter-spacing: 1px;
  }
  .address { margin-top: 10px; padding-left: 4px; font-size: 21px; }
</style>
</head>
<body>
<main class="flyer">
  <svg class="hero-shapes" viewBox="0 0 978 600" aria-hidden="false">
    <polygon points="0,0 628,0 628,292 248,572 0,328" fill="var(--gold)"/>
    <polygon points="0,0 609,0 609,282 248,548 0,310" fill="var(--white)"/>
    <polygon role="img" aria-label="Photo of an ambulance with lights on driving through a tunnel" points="0,0 609,0 609,272 248,538 0,300" fill="url(#heroPhoto)"/>
    <polygon points="609,0 978,0 833,262" fill="var(--white)"/>
    <defs>
      <linearGradient id="heroPhoto" x1="0" y1="0" x2="1" y2="1">
        <stop offset="0" stop-color="#3c5a85"/>
        <stop offset="0.45" stop-color="#dfe3e8"/>
        <stop offset="0.75" stop-color="#c8472f"/>
        <stop offset="1" stop-color="#1d2b45"/>
      </linearGradient>
    </defs>
  </svg>

  <svg class="badge-24" viewBox="0 0 150 110" aria-label="24/7 for emergency call outs">
    <path d="M30 70 A48 48 0 1 1 122 62" fill="none" stroke="var(--navy)" stroke-width="6"/>
    <text x="76" y="62" text-anchor="middle" font-family="Bebas Neue, Impact, sans-serif" font-size="54" fill="var(--navy)">24/7</text>
    <polygon points="0,72 150,58 146,82 4,96" fill="var(--navy)"/>
    <text x="75" y="84" text-anchor="middle" font-family="Bebas Neue, Impact, sans-serif" font-size="15" fill="var(--white)" transform="rotate(-5 75 80)">FOR EMERGENCY CALL OUTS</text>
  </svg>

  <h1 class="headline">Emergency<br>Medical Services</h1>
  <p class="intro">CareSwift Transit Health Services provides ambulance and mobility assistance vehicle transportation services to and from healthcare facilities as well as event standby and healthcare training through our training center (cpr, professional continuing education courses).</p>

  <section class="services">
    <div class="service">
      <svg viewBox="0 0 64 54" fill="none" stroke="#fff" stroke-width="3">
        <path d="M20 44 V28 A12 12 0 0 1 44 28 V44 Z" fill="#fff"/>
        <line x1="14" y1="48" x2="50" y2="48"/>
        <line x1="32" y1="2" x2="32" y2="10"/><line x1="10" y1="12" x2="16" y2="17"/><line x1="54" y1="12" x2="48" y2="17"/>
        <line x1="4" y1="30" x2="11" y2="30"/><line x1="53" y1="30" x2="60" y2="30"/>
        <line x1="32" y1="28" x2="32" y2="36" stroke="var(--red)"/><circle cx="32" cy="40" r="1.5" fill="var(--red)" stroke="none"/>
      </svg>
      <div class="service-label">Emergency<br>Medical Services</div>
    </div>
    <div class="service">
      <svg viewBox="0 0 64 54" fill="#fff">
        <path d="M4 10 H40 V18 H50 L60 30 V44 H4 Z"/>
        <circle cx="16" cy="46" r="6" fill="var(--red)" stroke="#fff" stroke-width="3"/>
        <circle cx="48" cy="46" r="6" fill="var(--red)" stroke="#fff" stroke-width="3"/>
        <path d="M19 18 h6 v6 h6 v6 h-6 v6 h-6 v-6 h-6 v-6 h6 Z" fill="var(--red)"/>
      </svg>
      <div class="service-label">Medical<br>Transportation</div>
    </div>
    <div class="service">
      <svg viewBox="0 0 64 54" fill="none" stroke="#fff" stroke-width="3">
        <rect x="6" y="6" width="38" height="28"/>
        <polyline points="12,26 20,18 27,23 37,12"/>
        <line x1="20" y1="34" x2="14" y2="48"/><line x1="30" y1="34" x2="36" y2="48"/>
        <path d="M40 36 L52 30 L64 36 L52 42 Z" fill="#fff"/>
        <path d="M45 39 V46 Q52 50 59 46 V39" />
      </svg>
      <div class="service-label">Education &amp;<br>Training Services</div>
    </div>
    <div class="service">
      <svg viewBox="0 0 64 54" fill="none" stroke="#fff" stroke-width="3">
        <path d="M24 12 V6 H40 V12"/>
        <rect x="12" y="12" width="40" height="36" rx="6" fill="#fff"/>
        <path d="M29 20 h6 v7 h7 v6 h-7 v7 h-6 v-7 h-7 v-6 h7 Z" fill="var(--red)" stroke="none"/>
      </svg>
      <div class="service-label">Special Events<br>&amp; Medical Standby</div>
    </div>
  </section>

  <div class="divider"></div>
  <section class="gallery">
    <div class="gallery-photo photo-stretcher" role="img" aria-label="Photo of paramedics loading a stretcher into an ambulance"></div>
    <div class="gallery-photo photo-standby" role="img" aria-label="Photo of a medical response team member on standby at an outdoor event"></div>
    <div class="gallery-photo photo-paramedic" role="img" aria-label="Photo of a paramedic in a high-visibility jacket beside an ambulance"></div>
  </section>

  <footer class="footer">
    <svg class="footer-shapes" viewBox="0 0 978 152" aria-hidden="true">
      <rect x="0" y="124" width="978" height="28" fill="var(--red)"/>
      <polygon points="498,0 978,0 978,152 432,152" fill="var(--navy)"/>
    </svg>
    <div class="brand">
      <span class="brand-mark"></span>
      <span class="brand-name">CareSwift Transit<br>Health Services</span>
    </div>
    <div class="contact">
      <div class="phone-line">
        <svg class="phone-icon" viewBox="0 0 28 44" fill="none" stroke="#fff" stroke-width="3">
          <rect x="2" y="2" width="24" height="40" rx="4"/>
          <line x1="2" y1="34" x2="26" y2="34"/><line x1="2" y1="8" x2="26" y2="8"/>
        </svg>
        <span class="phone">(555) 014-2287</span>
      </div>
      <p class="address">418 Larkmoor Ave Fairbrook NJ 07090</p>
    </div>
  </footer>
</main>
</body>
</html>
```